依頼詳細
今回は」取り急ぎ3種類の用途のメッセージカードのデザイン作成の依頼です。
メッセージカードに入れる文章も決まっていますのでその内容も入れての作成をお願いします。追加の依頼として14種類のメッセージカードの依頼もありますのでよろしくお願いします。
記載項目
株式会社マツバネ贈答
担当:田辺
TEL025-275-1277 FAX025-275-1350
Email:kenji@matsubanezoto.example.jp
希望イメージ
シンプル 複雑
単色 カラフル
暗い 明るい
日常 高級
遊び心 厳粛
未来的 伝統的
女性的 男性的
希望する色
設定なし
納品ファイル
• イラストレーター形式 (.ai)
• フォトショップ形式 (.psd)
• PNG形式 (.png)
補足説明
メッセージカードに入れる文章を添付しますので、よろしくお願いします。
また、参考までに今現在使用しているメッセージカードを添付します。
全く違うイメージでOKです。逆に異なった方がいいです。
サイズ:B7サイズ 91 × 128 ミリ
■ 選んだ理由

ご用途に合った上品なデザインが素敵でした。
年配の方への贈り物が多いので、特に還暦・長寿が派手過ぎず華やかで好感が持てました。

■ 提案者全員のお礼・コメント

たくさんのご提案をいただき、誠にありがとうございました。
どれも素敵なデザインでしたので選出にかなり迷いました。
他の用途でも依頼が出来たらと思いますので、またご縁がございましたらよろしくお願い致します。

```html
<!DOCTYPE html>
<html lang="ja">
<head>
<meta charset="UTF-8">
<title>祝退職 メッセージカード</title>
<link rel="stylesheet" href="https://fonts.googleapis.com/css2?family=Shippori+Mincho+B1:wght@500;700&display=swap">
<style>
  :root {
    --paper: #fbf6ec;
    --tint-pink: #f6dcd6;
    --tint-blue: #dbe9ec;
    --tint-gold: #f5e6c4;
    --ink: #3a3230;
    --accent-red: #b3243a;
    --flower-crimson: #b42a4c;
    --flower-teal: #2f6a62;
    --flower-aqua: #5cc3c8;
    --flower-orange: #f0a531;
  }
  html, body {
    margin: 0;
    padding: 0;
    overflow: hidden;
  }
  body {
    width: 853px;
    height: 1200px;
  }
  .card {
    position: relative;
    width: 853px;
    height: 1200px;
    overflow: hidden;
    background:
      radial-gradient(circle at 20% 15%, var(--tint-pink) 0%, transparent 45%),
      radial-gradient(circle at 80% 30%, var(--tint-blue) 0%, transparent 45%),
      radial-gradient(circle at 30% 80%, var(--tint-gold) 0%, transparent 50%),
      var(--paper);
    font-family: "Shippori Mincho B1", serif;
    color: var(--ink);
  }
  .card-title {
    position: absolute;
    top: 168px;
    left: 398px;
    margin: 0;
    font-size: 112px;
    font-weight: 700;
    letter-spacing: 0.02em;
    line-height: 1.2;
    z-index: 2;
  }
  .card-title .celebrate {
    color: var(--accent-red);
  }
  .card-message {
    position: absolute;
    top: 112px;
    left: 150px;
    width: 230px;
    height: 910px;
    margin: 0;
    writing-mode: vertical-rl;
    font-size: 34px;
    font-weight: 500;
    line-height: 1.9;
    letter-spacing: 3px;
    z-index: 2;
  }
  .card-message p {
    margin: 0;
  }
  .floral-art {
    position: absolute;
    left: 300px;
    top: 412px;
    width: 553px;
    height: 788px;
    z-index: 1;
  }
</style>
</head>
<body>
  <main class="card">
    <h1 class="card-title"><span class="celebrate">祝</span>退職</h1>

    <div class="card-message">
      <p>ご退職おめでとうございます。</p>
      <p>感謝の気持ちを込めて、</p>
      <p>ささやかな「記念品」をお贈りさせていただきます。</p>
      <p>ご笑納頂けると幸いです。</p>
    </div>

    <svg class="floral-art" viewBox="0 0 553 788" role="img" aria-label="赤・水色・橙の花と深緑の葉を束ねた華やかな花のイラスト">
      <defs>
        <radialGradient id="floral-fill" cx="62%" cy="62%" r="60%">
          <stop offset="0%" stop-color="var(--flower-crimson)"/>
          <stop offset="35%" stop-color="var(--flower-orange)" stop-opacity="0.85"/>
          <stop offset="65%" stop-color="var(--flower-aqua)" stop-opacity="0.7"/>
          <stop offset="100%" stop-color="var(--flower-teal)" stop-opacity="0.4"/>
        </radialGradient>
      </defs>
      <path d="M553 60 C480 90 420 60 330 20 C250 60 210 150 250 260 C170 300 110 400 120 500 C60 560 20 660 0 788 L553 788 Z" fill="url(#floral-fill)"/>
    </svg>
  </main>
</body>
</html>
```